Drumm's Accord business card design

I am a private mediator and family dispute resolution practitioner. I am located on Gold Coast, Australia. Private mediation is mandatory within the Household Relations Code so I offer very affordable private mediation for families and workplace and community. We also offer education and workshops training and development for schools, families and businesses based on becoming more open and effective communicator and anti conflict resolution, dispute resolution. We facilitate crucial conversations and help families create parenting agreements/plans about their children and situation and people to live in harmony even though they may disagree. We would like to see designs that are simple that use vibrant pink/purple, poppy red and vibrant blue (colour of communication) or yellow or vibrant lime green. We would like the design represent new growth, moving forward in separate ways but harmony similar to a seed (circle open at the top) with new shoots in opposite direction. The final design should communicate moving forward in slightly different ways with the principle from family represented by seed or something similar.

Drumm's Accord, Helen Drumm,PO Box 152, Robina Qld 4226Effective Private Mediation, Anti Conflict Coaching, Couples and individual coaching. family | workplace | community Competitive rates | after hour appointments. Nationally Accredited Mediator, Family Dispute Resolution Practitioner M: 0427518260 E: helendrumm4@quellmail.com

Sans Serif

a64599
fbed22
ec1f27
fff5ef

Must have
• colour and be double sided
• vibrant poppy colour red is my preference blended or contrasted with purple or other contrast colour
• elegant professional font cannot add file for some reason below under image or sketch but google images have good variety of red/orange colour of poppy flower that I like
Nice to have
• graduated colour from left to right
Should not have
• no capital/ block text that look solid or chunky

```html
<!DOCTYPE html>
<html lang="en">
<head>
<meta charset="utf-8">
<title>Drumm's Accord — Business Card</title>
<link rel="stylesheet" href="https://fonts.googleapis.com/css2?family=Open+Sans:wght@400;600&display=swap">
<style>
  :root {
    --backdrop: #2b2d31;
    --purple: #7b52a6;
    --purple-light: #e4d8f0;
    --poppy: #ec1f27;
    --card-white: #fbfbfb;
    --ink: #2a2a2a;
    --rule: #cfcfcf;
  }
  * { margin: 0; padding: 0; box-sizing: border-box; }
  html, body {
    width: 1200px; height: 864px; overflow: hidden;
    background: var(--backdrop);
    font-family: "Open Sans", Arial, sans-serif;
  }
  .stage { position: relative; width: 1200px; height: 864px; }

  .card {
    position: absolute;
    width: 600px; height: 340px;
    border-radius: 2px;
    overflow: hidden;
  }

  /* Front side */
  .card-front {
    left: 180px; top: 60px;
    background: var(--purple);
    display: flex; align-items: center; justify-content: center;
  }
  .front-name {
    display: flex; align-items: center; gap: 14px;
    color: var(--purple-light);
    font-weight: 600; font-size: 34px; letter-spacing: 0.5px;
  }
  .front-dot {
    width: 22px; height: 22px; border-radius: 50%;
    background: var(--poppy);
  }

  /* Back side */
  .card-back {
    left: 400px; top: 460px;
    background: var(--card-white);
  }
  .person { position: absolute; left: 40px; top: 92px; }
  .person-name { color: var(--purple); font-weight: 600; font-size: 24px; line-height: 1.15; }
  .person-role { color: var(--ink); font-size: 15px; }

  .brand {
    position: absolute; right: 40px; top: 80px;
    display: flex; align-items: center; gap: 10px;
    color: var(--purple);
    font-weight: 600; font-size: 26px; letter-spacing: 0.5px;
  }
  .brand-mark { width: 16px; height: 16px; border-radius: 50%; background: var(--poppy); }

  .divider {
    position: absolute; left: 40px; right: 40px; top: 168px;
    height: 2px;
    background: linear-gradient(90deg, var(--poppy), var(--purple));
  }

  .contacts {
    position: absolute; right: 40px; top: 190px;
    list-style: none;
    display: flex; flex-direction: column; align-items: flex-end; gap: 5px;
  }
  .contact {
    display: flex; align-items: center; gap: 10px;
    color: var(--ink); font-size: 15px; line-height: 20px;
  }
  .contact-icon {
    width: 19px; height: 19px; border-radius: 2px;
    background: var(--purple);
    display: flex; align-items: center; justify-content: center;
  }
  .contact-icon svg { width: 13px; height: 13px; }
</style>
</head>
<body>
<main class="stage">

  <section class="card card-front" aria-label="Card front">
    <div class="front-name"><span class="front-dot"></span>Drumm's Accord</div>
  </section>

  <section class="card card-back" aria-label="Card back">
    <div class="person">
      <p class="person-name">Marcus Hale</p>
      <p class="person-role">Managing Director</p>
    </div>

    <div class="brand"><span class="brand-mark"></span>Drumm's Accord</div>

    <div class="divider"></div>

    <ul class="contacts">
      <li class="contact">047-318-2265
        <span class="contact-icon"><svg viewBox="0 0 14 14" fill="#fff"><path d="M1 5c0-2 3-3 6-3s6 1 6 3v1h-3V4.5H4V6H1z"/><rect x="3" y="7" width="8" height="5" rx="1"/></svg></span></li>
      <li class="contact">159-630-4471
        <span class="contact-icon"><svg viewBox="0 0 14 14" fill="none" stroke="#fff" stroke-width="1.4"><rect x="3" y="2" width="8" height="4"/><rect x="2" y="6" width="10" height="6" rx="1"/></svg></span></li>
      <li class="contact">159-630-4471
        <span class="contact-icon"><svg viewBox="0 0 14 14" fill="none" stroke="#fff" stroke-width="1.4"><rect x="4" y="1.5" width="6" height="11" rx="1"/><line x1="6" y1="10.5" x2="8" y2="10.5"/></svg></span></li>
      <li class="contact">hello@drummsaccord.example
        <span class="contact-icon"><svg viewBox="0 0 14 14" fill="none" stroke="#fff" stroke-width="1.4"><rect x="1.5" y="3" width="11" height="8"/><polyline points="1.5,3 7,8 12.5,3"/></svg></span></li>
      <li class="contact">www.drummsaccord.example
        <span class="contact-icon"><svg viewBox="0 0 14 14" fill="none" stroke="#fff" stroke-width="1.5"><rect x="1.5" y="6" width="6" height="3.5" rx="1.7" transform="rotate(-45 4.5 7.75)"/><rect x="6.5" y="4.5" width="6" height="3.5" rx="1.7" transform="rotate(-45 9.5 6.25)"/></svg></span></li>
    </ul>
  </section>

</main>
</body>
</html>
```